Flyer for Merchant Capital Cash Advance business

Need Flyer Design to be advertised on Social Media Platforms and also Print it to Publish it in Magazines.
Flyer Will be printed in different sizes for different publications.
Size 1) 6.25 inches * 11 inches.
Size 2) 8 inch * 11 inch
Size 3) 8 inch * 5.5 I inch
Size 4) 5 inch * 7 inch.
Google “Merchant Capital Cash advance flyer pics” to get an idea.

Flyer Design for Merchant Cash advance business.

Merchant Cash Advance is alternate to bank loans and does not require Personal Guarantee or Collateral.

Target Market(s)

Business owners seeking loan.

Industry/Entity Type

Business Service

Font styles to use
Serif
Sans Serif
Decorative
Script

Colors

Designer to choose colors to be used in the design.

Requirements
Must have
• Content from the Files Uploaded.
• Sharp Colors.
Nice to have
• Would like to see flyer in shape of a Bank Check or a $100 Bill.
• Would like to show a Comparison between Bank Loan and MCA.
• Open to any other ideas.

```html
<!DOCTYPE html>
<html lang="en">
<head>
<meta charset="utf-8">
<title>Business Capital Cash Advance Flyer</title>
<link rel="stylesheet" href="https://fonts.googleapis.com/css2?family=Rye&family=Montserrat:wght@400;500&display=swap">
<style>
  :root {
    --page: #ffffff;
    --paper: #dcd7b2;
    --paper-light: #e4e0bf;
    --ornament: #a8a27b;
    --ornament-dark: #8e8963;
    --ink: #55533a;
    --ink-soft: #6b6a4d;
    --headline-fill: #8b8763;
    --rule: #9c987a;
    --yes: #2fa84a;
    --no: #d8373c;
    --photo-light: #ece6cf;
    --photo-mid: #b9c3cc;
  }
  * { box-sizing: border-box; margin: 0; padding: 0; }
  html, body { width: 1200px; height: 960px; overflow: hidden; background: var(--page); }
  body { position: relative; font-family: "Montserrat", sans-serif; color: var(--ink); }

  .flyer {
    position: absolute; left: 78px; top: 233px; width: 1046px; height: 493px;
    background: radial-gradient(ellipse at 50% 45%, var(--paper-light), var(--paper) 75%);
    box-shadow: 0 4px 14px rgba(0,0,0,0.25);
  }
  .frame-ornament {
    position: absolute; inset: 0;
    border: 30px solid var(--ornament);
    opacity: 0.55;
  }
  .frame-rule {
    position: absolute; left: 40px; right: 40px; top: 38px; bottom: 38px;
    border: 2px solid var(--ornament-dark); opacity: 0.6;
  }

  .headline {
    position: absolute; left: 0; right: 0; text-align: center;
    font-family: "Rye", serif; text-transform: uppercase;
    color: var(--headline-fill);
    -webkit-text-stroke: 1.4px var(--ink);
    letter-spacing: -0.5px; white-space: nowrap;
  }
  .headline-1 { top: 33px; font-size: 30px; }
  .headline-2 { top: 69px; font-size: 30px; }
  .tagline {
    position: absolute; left: 0; right: 0; top: 113px; text-align: center;
    font-family: "Rye", serif; font-size: 21px; color: var(--ink-soft);
    text-transform: uppercase; white-space: nowrap;
  }

  .photo {
    position: absolute; left: 82px; top: 162px; width: 286px; height: 244px;
    border: 1px solid var(--rule);
    background: linear-gradient(135deg, var(--photo-light) 0%, var(--photo-mid) 100%);
  }

  .compare {
    position: absolute; left: 406px; top: 160px; width: 546px;
    border-collapse: collapse; border: 1.5px solid var(--rule);
  }
  .compare td, .compare th { border: 1.5px solid var(--rule); }
  .compare th {
    height: 46px; font-weight: 400; color: var(--ink-soft);
  }
  .compare .title-cell {
    text-align: left; padding-left: 14px; font-size: 24px; width: 354px;
  }
  .compare .col-head { font-size: 17px; line-height: 17px; width: 107px; }
  .compare .col-head.bank { width: 85px; }
  .compare td { height: 28px; font-size: 13.5px; color: #2e2d1e; }
  .compare .feature { padding-left: 14px; }
  .compare .mark { text-align: center; }
  .compare .mark svg { width: 17px; height: 17px; vertical-align: middle; }
  .compare tr.tall td { height: 37px; line-height: 14px; }

  .footer { position: absolute; top: 423px; font-size: 15.5px; color: #2e2d1e; white-space: nowrap; }
  .business-name { left: 90px; top: 420px; font-size: 19.5px; font-weight: 500; color: var(--ink-soft); }
  .phone { left: 532px; }
  .email { left: 736px; }
  .footer svg { width: 14px; height: 14px; vertical-align: -1px; margin-right: 8px; fill: var(--ink-soft); }
</style>
</head>
<body>
<svg width="0" height="0" style="position:absolute">
  <defs>
    <symbol id="tick" viewBox="0 0 20 20">
      <circle cx="10" cy="10" r="8.3" fill="none" stroke="var(--yes)" stroke-width="1.8"/>
      <path d="M6 10.2l3 3 6-7" fill="none" stroke="var(--yes)" stroke-width="1.9" stroke-linecap="round" stroke-linejoin="round"/>
    </symbol>
    <symbol id="cross" viewBox="0 0 20 20">
      <circle cx="10" cy="10" r="8.3" fill="none" stroke="var(--no)" stroke-width="1.3"/>
      <path d="M7 7l6 6M13 7l-6 6" stroke="var(--no)" stroke-width="1.3" stroke-linecap="round"/>
    </symbol>
  </defs>
</svg>

<main class="flyer">
  <div class="frame-ornament" role="img" aria-label="Engraved banknote-style ornamental border"></div>
  <div class="frame-rule"></div>

  <h1 class="headline headline-1">A Convenient Alternative to Bank Loan</h1>
  <h2 class="headline headline-2">Business&nbsp; Capital Cash Advance</h2>
  <p class="tagline">Business Funding Made Easy</p>

  <div class="photo" role="img" aria-label="Photo of an advisor meeting a young couple at a desk"></div>

  <table class="compare">
    <tr>
      <th class="title-cell">Business Capital</th>
      <th class="col-head">Cash<br>Advance</th>
      <th class="col-head bank">Bank<br>Loan</th>
    </tr>
    <tr><td class="feature">No Personal Guarantee</td><td class="mark"><svg><use href="#tick"/></svg></td><td class="mark"><svg><use href="#cross"/></svg></td></tr>
    <tr><td class="feature">No Collateral &nbsp;or Guarantors</td><td class="mark"><svg><use href="#tick"/></svg></td><td class="mark"><svg><use href="#cross"/></svg></td></tr>
    <tr><td class="feature">Simple One Page Application</td><td class="mark"><svg><use href="#tick"/></svg></td><td class="mark"><svg><use href="#cross"/></svg></td></tr>
    <tr><td class="feature">No Interest Rate (Flat Fee)</td><td class="mark"><svg><use href="#tick"/></svg></td><td class="mark"><svg><use href="#cross"/></svg></td></tr>
    <tr><td class="feature">Bankcruptcy OK</td><td class="mark"><svg><use href="#tick"/></svg></td><td class="mark"><svg><use href="#cross"/></svg></td></tr>
    <tr><td class="feature">No Minimum Credit Score Required</td><td class="mark"><svg><use href="#tick"/></svg></td><td class="mark"><svg><use href="#cross"/></svg></td></tr>
    <tr class="tall"><td class="feature">Opportunity to renew your cash<br>advance for additional funds</td><td class="mark"><svg><use href="#tick"/></svg></td><td class="mark"><svg><use href="#cross"/></svg></td></tr>
  </table>

  <p class="footer business-name">Business Name Area</p>
  <p class="footer phone"><svg viewBox="0 0 24 24"><path d="M6.6 10.8a15.1 15.1 0 0 0 6.6 6.6l2.2-2.2a1 1 0 0 1 1-.25 11.4 11.4 0 0 0 3.6.57 1 1 0 0 1 1 1V20a1 1 0 0 1-1 1A17 17 0 0 1 3 4a1 1 0 0 1 1-1h3.5a1 1 0 0 1 1 1c0 1.25.2 2.45.57 3.57a1 1 0 0 1-.25 1z"/></svg>555-0148-226</p>
  <p class="footer email"><svg viewBox="0 0 24 18"><path d="M0 0h24v2L12 10 0 2z M0 4l12 8 12-8v14H0z"/></svg>hello@fundingdesk.example</p>
</main>
</body>
</html>
```